Travel Company is looking for a STAND OUT Business Card

I need a unique Business Card that will truly stand out. Nothing too busy. Simple is good, right? Not looking for a standard design either. No cookie cutter layout. We are a Travel Company that works more with Companies than Travelers. I had an idea to focus and emphasis on the 2 logo a bit more. This is not necessary, however thought it would look interesting. I am just looking for something interesting and a bit different. Does't have to completely off the wall crazy, just not your run of the mill business card.

Target Market(s)

Hoteliers, Resort Management, Call Centers, Executives, Travelers, Families, Businesses

Industry/Entity Type

Hospitality

Contact Information for Business Card

President/CEO - Marcus T Bellamy (title not necessary if design doesn't allow for it)
contact - (407) 555-0186
email - mbellamy@wayfarenow.example
address - 4812 Quillmore Ave #164
Orlando, FL 32804
website - www.wayfarenow.example

Font styles to use
Serif
Other font styles liked:
• Avenir Next LT Pro BOLD

Requirements
Must have
• simple look and design. Unique design
Nice to have
• I attached the 2 logo separate from the main logo. This can be used separately from the Main Logo, together with the main logo or as main logo. I included the logo font. Use it or not, designers choice.
Should not have
• cookie cutter design. Little use of red other than the logo

```html
<!DOCTYPE html>
<html lang="en">
<head>
<meta charset="utf-8">
<title>Wayfarenow Business Card</title>
<link rel="stylesheet" href="https://fonts.googleapis.com/css2?family=Oswald:wght@600&family=Barlow+Semi+Condensed:wght@400;700&family=Barlow:wght@400&display=swap">
<style>
  :root {
    --red: #f40d00;
    --ink: #111111;
    --panel-black: #080909;
    --row-1: #191c1d;
    --row-2: #1f2224;
    --row-3: #25292b;
    --paper: #ffffff;
    --backdrop: #e3e7e8;
    --muted: #d9d9d9;
  }
  html, body { margin: 0; padding: 0; overflow: hidden; }
  body {
    width: 1200px; height: 1200px;
    background: var(--backdrop);
    position: relative;
    font-family: "Barlow Semi Condensed", sans-serif;
  }
  .card {
    position: absolute; top: 150px;
    width: 540px; height: 900px;
    overflow: hidden;
  }
  .card--front { left: 40px; background: var(--paper); }
  .card--back { left: 620px; background: var(--ink); }

  .brand-band {
    position: absolute; left: 0; width: 100%;
    background: var(--red);
  }
  .card--front .brand-band { top: 176px; height: 40px; }
  .card--back .brand-band { top: 326px; height: 187px; }

  .wordmark {
    position: absolute; left: 50%; transform: translateX(-50%);
    background: var(--paper);
    display: flex; align-items: center; justify-content: center; gap: 14px;
    color: var(--ink);
    font-family: "Barlow Semi Condensed", sans-serif;
    font-weight: 700;
    letter-spacing: -1px;
    white-space: nowrap;
  }
  .wordmark__dot { border-radius: 50%; background: var(--red); flex: none; }
  .card--front .wordmark { top: 156px; height: 80px; padding: 0 8px; font-size: 64px; }
  .card--front .wordmark__dot { width: 26px; height: 26px; }
  .card--back .wordmark { top: 274px; width: 429px; height: 290px; font-size: 72px; }
  .card--back .wordmark__dot { width: 30px; height: 30px; }

  .name-panel {
    position: absolute; top: 364px; left: 0; width: 100%; height: 128px;
    background: var(--panel-black); text-align: center;
  }
  .name-panel__name {
    margin: 0; padding-top: 30px;
    font-family: "Oswald", sans-serif; font-weight: 600;
    font-size: 38px; line-height: 1; color: #fff; letter-spacing: -0.5px;
    transform: scaleX(0.86);
  }
  .name-panel__title {
    margin: 4px 0 0;
    font-family: "Barlow", sans-serif; font-size: 15px;
    color: var(--red); letter-spacing: 0.5px;
  }

  .contact-row { position: absolute; left: 0; width: 100%; }
  .contact-row--address { top: 492px; height: 128px; background: var(--row-1); }
  .contact-row--phone { top: 620px; height: 128px; background: var(--row-2); }
  .contact-row--web { top: 748px; height: 122px; background: var(--row-3); }

  .contact-row__text {
    position: absolute; left: 270px; top: 50%;
    transform: translate(-50%, -50%);
    margin: 0; text-align: center; white-space: nowrap;
    color: var(--muted); font-size: 24px; line-height: 31px; letter-spacing: 0.3px;
  }
  .contact-row--web .contact-row__text {
    left: 296px; font-size: 22px; letter-spacing: 0;
  }
  .contact-icon {
    position: absolute; top: 50%; transform: translate(-50%, -50%);
    width: 64px; height: 64px; box-sizing: border-box;
    border: 2px solid var(--red); border-radius: 50%;
    display: flex; align-items: center; justify-content: center;
  }
  .contact-row--address .contact-icon { left: 96px; }
  .contact-row--phone .contact-icon { left: 445px; }
  .contact-row--web .contact-icon { left: 93px; }

  .front-footer-band {
    position: absolute; bottom: 0; left: 0; width: 100%; height: 30px;
    background: var(--red);
  }
  .back-url {
    position: absolute; top: 806px; left: 0; width: 100%;
    text-align: center; margin: 0;
    color: #fff; font-size: 26px; letter-spacing: 0.4px;
  }
</style>
</head>
<body>
  <section class="card card--front">
    <div class="brand-band"></div>
    <div class="wordmark"><span class="wordmark__dot"></span>wayfarenow</div>

    <header class="name-panel">
      <h1 class="name-panel__name">MARCUS T BELLAMY</h1>
      <p class="name-panel__title">PRESIDENT/CEO</p>
    </header>

    <div class="contact-row contact-row--address">
      <span class="contact-icon">
        <svg width="32" height="30" viewBox="0 0 32 30" aria-hidden="true">
          <path d="M16 2 L1 15 L4 18 L16 7.5 L28 18 L31 15 Z" fill="#fff"/>
          <path d="M6 17 L16 9 L26 17 V28 H19 V21 H13 V28 H6 Z" fill="#fff"/>
        </svg>
      </span>
      <p class="contact-row__text">4812 Quillmore Ave #164<br>Orlando, FL 32804</p>
    </div>

    <div class="contact-row contact-row--phone">
      <p class="contact-row__text">(407) 555-0186</p>
      <span class="contact-icon">
        <svg width="34" height="28" viewBox="0 0 34 28" aria-hidden="true">
          <path d="M2 9 C2 3 32 3 32 9 L32 12 L25 12 L25 8 L9 8 L9 12 L2 12 Z" fill="#fff"/>
          <path d="M10 11 H24 L29 20 V26 H5 V20 Z" fill="#fff"/>
          <g fill="#191c1d">
            <circle cx="14" cy="16" r="1.2"/><circle cx="17" cy="16" r="1.2"/><circle cx="20" cy="16" r="1.2"/>
            <circle cx="14" cy="19" r="1.2"/><circle cx="17" cy="19" r="1.2"/><circle cx="20" cy="19" r="1.2"/>
            <circle cx="14" cy="22" r="1.2"/><circle cx="17" cy="22" r="1.2"/><circle cx="20" cy="22" r="1.2"/>
          </g>
        </svg>
      </span>
    </div>

    <div class="contact-row contact-row--web">
      <span class="contact-icon">
        <svg width="34" height="34" viewBox="0 0 34 34" aria-hidden="true" fill="none" stroke="#fff" stroke-width="2.2">
          <circle cx="17" cy="17" r="15"/>
          <ellipse cx="17" cy="17" rx="7" ry="15"/>
          <line x1="17" y1="2" x2="17" y2="32"/>
          <line x1="2" y1="17" x2="32" y2="17"/>
          <line x1="4.5" y1="10" x2="29.5" y2="10"/>
          <line x1="4.5" y1="24" x2="29.5" y2="24"/>
        </svg>
      </span>
      <p class="contact-row__text">mbellamy@wayfarenow.example<br>www.wayfarenow.example</p>
    </div>

    <div class="front-footer-band"></div>
  </section>

  <section class="card card--back">
    <div class="brand-band"></div>
    <div class="wordmark"><span class="wordmark__dot"></span>wayfarenow</div>
    <p class="back-url">www.wayfarenow.example</p>
  </section>
</body>
</html>
```